Business card design incorporating discount offer

We are a trade services company and we need a double sided business card that is going to be used by our tradesmen to give to customers on completion of their jobs.

Below are the key elements of the card that we would like to include:

-Main logo with text 'Expert Property Care' underneath.
-Up to 12 smaller icon logos with text 'Your local all-trade experts' to emphasise the point that we cover all the trades
-Discount offer - 10% discount
-Telephone number and website address
-Blank space for tradesman to enter his/her name
-Request for customer feedback with feedback url

This business card will be printed on regular card. In the past we have favoured designs that use a black background but we're open to new ideas.

I have attached a few files:

-A simple wire frame example to show how this card could look with the different elements mentioned above, feel free to use a layout similar to this or come up with something totally different (biz-card.pdf)
-Front and back of a loyalty card the we've used in the past (this card was printed on plastic)
-Front and back of a key fob design that we've previously used (this card was printed on plastic)
-A logo file with the 12 small icons and the main logo image

If you need further images or information please ask.

```html
<!DOCTYPE html>
<html lang="en">
<head>
<meta charset="utf-8">
<title>HKT Business Card – Front and Back</title>
<link href="https://fonts.googleapis.com/css2?family=Open+Sans:wght@400;600;700;800&display=swap" rel="stylesheet">
<style>
  :root {
    --canvas: #d8d3cb;
    --card-black: #141518;
    --card-black-soft: #23252a;
    --brand-blue: #1ba3e6;
    --brand-blue-deep: #0c72b4;
    --text-white: #ffffff;
    --text-grey: #c9ccd2;
    --tile-purple: #9b4fc4;
    --tile-red: #e0413c;
    --tile-teal: #27b3a6;
    --tile-green: #7cc242;
    --tile-orange: #f39a1e;
    --tile-yellow: #f2c73b;
    --tile-grey: #8d949c;
    --tile-blue: #3f7fd8;
    --tile-pink: #e2508d;
    --tile-sky: #5cc6f0;
  }
  * { box-sizing: border-box; margin: 0; padding: 0; }
  html, body {
    width: 704px; height: 1200px; overflow: hidden;
    background: var(--canvas);
    font-family: "Open Sans", Arial, sans-serif;
  }
  .card {
    position: absolute; left: 82px;
    width: 540px; height: 320px;
    border-radius: 14px;
    background: linear-gradient(160deg, var(--card-black-soft), var(--card-black) 60%);
    overflow: hidden;
    box-shadow: 0 10px 28px rgba(0,0,0,.35);
    color: var(--text-white);
  }
  .card--front { top: 140px; }
  .card--back { top: 740px; }

  /* Front */
  .offer-ribbon {
    position: absolute; top: 0; right: 34px;
    width: 196px; height: 236px;
    background: linear-gradient(180deg, var(--brand-blue), var(--brand-blue-deep));
    clip-path: polygon(0 0, 100% 0, 100% 100%, 50% 82%, 0 100%);
    text-align: center; padding-top: 22px;
  }
  .offer-percent { font-size: 66px; font-weight: 800; line-height: 1; letter-spacing: -1px; }
  .offer-title { font-size: 19px; font-weight: 700; line-height: 1.15; margin-top: 6px; }
  .offer-note { font-size: 12px; font-weight: 600; line-height: 1.25; margin-top: 6px; }

  .brand { position: absolute; left: 34px; top: 96px; }
  .brand-name { display: flex; align-items: center; gap: 12px; }
  .brand-dot { width: 46px; height: 46px; border-radius: 50%; background: var(--brand-blue); }
  .brand-word { font-size: 58px; font-weight: 700; line-height: 1; }
  .brand-tagline { font-size: 25px; font-weight: 600; margin-top: 12px; }

  .contact { position: absolute; left: 34px; bottom: 30px; font-size: 17px; line-height: 1.35; display: flex; gap: 10px; align-items: center; }
  .contact svg { width: 26px; height: 26px; fill: var(--text-white); }

  /* Back */
  .trade-panel {
    position: absolute; left: 0; top: 0; bottom: 0; width: 200px;
    background: linear-gradient(180deg, var(--brand-blue), var(--brand-blue-deep));
    display: grid; grid-template-columns: repeat(3, 48px); grid-auto-rows: 48px;
    gap: 14px; align-content: center; justify-content: center;
  }
  .trade-tile { border-radius: 10px; box-shadow: 0 2px 4px rgba(0,0,0,.25); }
  .details { position: absolute; left: 224px; right: 26px; top: 34px; }
  .details-heading { font-size: 22px; font-weight: 700; }
  .tradesman-label { font-size: 12px; color: var(--brand-blue); margin-top: 22px; }
  .tradesman-field { height: 36px; background: var(--text-white); border-radius: 3px; margin-top: 4px; }
  .feedback-question { font-size: 17px; color: var(--brand-blue); font-weight: 600; margin-top: 26px; }
  .feedback-ask { font-size: 16px; margin-top: 8px; }
  .feedback-url { font-size: 16px; margin-top: 4px; color: var(--text-grey); }
</style>
</head>
<body>

<section class="card card--front" aria-label="Business card front">
  <div class="offer-ribbon">
    <div class="offer-percent">10%</div>
    <div class="offer-title">discount<br>with this card</div>
    <div class="offer-note">check our web site<br>for full offer details</div>
  </div>

  <div class="brand">
    <div class="brand-name">
      <span class="brand-dot"></span>
      <span class="brand-word">HKT</span>
    </div>
    <div class="brand-tagline">Expert Property Care</div>
  </div>

  <div class="contact">
    <svg viewBox="0 0 24 24" aria-hidden="true"><path d="M6.6 10.8a15.1 15.1 0 0 0 6.6 6.6l2.2-2.2c.3-.3.7-.4 1-.2 1.1.4 2.3.6 3.6.6.6 0 1 .4 1 1V20c0 .6-.4 1-1 1A17 17 0 0 1 3 4c0-.6.4-1 1-1h3.5c.6 0 1 .4 1 1 0 1.3.2 2.5.6 3.6.1.3 0 .7-.2 1z"/></svg>
    <div>0800 555 0192<br>hkt-homecare.co.uk</div>
  </div>
</section>

<section class="card card--back" aria-label="Business card back">
  <div class="trade-panel" role="img" aria-label="Twelve trade service icons">
    <span class="trade-tile" style="background:var(--tile-purple)"></span>
    <span class="trade-tile" style="background:var(--tile-red)"></span>
    <span class="trade-tile" style="background:var(--tile-teal)"></span>
    <span class="trade-tile" style="background:var(--tile-yellow)"></span>
    <span class="trade-tile" style="background:var(--tile-orange)"></span>
    <span class="trade-tile" style="background:var(--tile-grey)"></span>
    <span class="trade-tile" style="background:var(--tile-green)"></span>
    <span class="trade-tile" style="background:var(--tile-sky)"></span>
    <span class="trade-tile" style="background:var(--tile-blue)"></span>
    <span class="trade-tile" style="background:var(--tile-pink)"></span>
    <span class="trade-tile" style="background:var(--tile-grey)"></span>
    <span class="trade-tile" style="background:var(--tile-yellow)"></span>
  </div>

  <div class="details">
    <h2 class="details-heading">Your local all-trade experts</h2>
    <p class="tradesman-label">Your HKT tradesman:</p>
    <div class="tradesman-field"></div>
    <p class="feedback-question">What do you think about our service?</p>
    <p class="feedback-ask">Please leave feedback online</p>
    <p class="feedback-url">www.hkt-homecare.co.uk/feedback</p>
  </div>
</section>

</body>
</html>
```